Vitamin and Nutrition Ecommerce Site Needs a High End Website Design

We need a new and improved Homepage design for a leading Vitamin eCommerce business.
We supply our customers worldwide with leading brands of vitamin supplements and nutritional products at discounted prices.
The site design and layout must improve sales conversion and maximize the user experience staying on the site!

We will need to see;
A New Nutri Harbour stylized font (no logo)
High-End Modern Design
Easy Sales Conversion Experience
Excellent Layout, Fast Navigation
Quality Font style, Stylish Colour Palette Selection
Appropriate Spacing
Call To Action to Improve Sales Conversion
Web page should Look Clean and Minimalist

The design should improve sales, communicate easy to find products, facilitate fast ordering, have a modern and professional appearance centered toward a predominately female consumer.

Thank you for your interest in this project!

Current design can be found on this link;
www.nutriharbour.com.au/nutri/

Target Market(s)

80% Female 30-65 years

Industry/Entity Type

Business

Number of Pages Required

1 page

Colors

Designer to choose colors to be used in the design.

Requirements
Must have
• design must result improve sales conversion
• new Nutri Harbour font design
• search field
• attractive clean modern design
• stylish font and colour palette selection
Nice to have
• white background
Should not have
• cluttered or busy layout
• confusing navigation

```html
<!DOCTYPE html>
<html lang="en">
<head>
<meta charset="utf-8">
<title>Nutri Harbour – Vitamins &amp; Supplements</title>
<link href="https://fonts.googleapis.com/css2?family=Roboto:wght@300;400;500;700&family=Roboto+Condensed:wght@400;700&family=Raleway:wght@300;400&family=Cinzel:wght@400;700&display=swap" rel="stylesheet">
<style>
:root{
  --green:#6ab04c;
  --green-dark:#5a9a3e;
  --orange:#f47b20;
  --orange-hero:#f5822a;
  --sky:#4fb6e3;
  --sky-band:#5bbfe6;
  --ink:#222;
  --text:#444;
  --muted:#777;
  --line:#dcdcdc;
  --panel:#e6e6e6;
  --footer:#f3f3f3;
  --white:#fff;
}
*{box-sizing:border-box;margin:0;padding:0}
html,body{width:878px;height:1200px;overflow:hidden;background:var(--white)}
body{font-family:'Roboto',sans-serif;color:var(--text);position:relative}
.wrap{width:770px;margin:0 auto;position:relative}

/* top bar */
.topbar{height:24px;border-bottom:1px solid var(--line);font-size:10px;color:#555}
.topbar .wrap{display:flex;justify-content:space-between;align-items:center;height:24px}
.topbar .promo{padding-left:5px}
.topbar .links{display:flex;height:24px}
.topbar .links span{display:flex;align-items:center;gap:5px;padding:0 10px;border-left:1px solid var(--line)}
.topbar .links span:last-child{border-right:1px solid var(--line)}
.topbar svg{width:9px;height:9px}

/* header */
.header{height:74px}
.header .wrap{display:flex;align-items:center;height:74px}
.brand{display:flex;align-items:center;gap:8px;width:286px}
.brand .dot{width:18px;height:18px;border-radius:50%;background:var(--green)}
.brand .name{font-family:'Raleway',sans-serif;font-weight:400;font-size:27px;color:#555;letter-spacing:-.3px}
.search{display:flex;width:244px;height:27px;border:1px solid var(--line)}
.search .field{flex:1;font-size:10px;color:#555;padding:0 8px;display:flex;align-items:center}
.search .btn{width:27px;background:var(--orange);display:flex;align-items:center;justify-content:center}
.cart{margin-left:auto;width:111px;height:47px;background:var(--sky);display:flex;color:var(--white)}
.cart .icon{width:50px;display:flex;align-items:center;justify-content:center;border-right:1px solid rgba(255,255,255,.5)}
.cart .info{flex:1;text-align:center;padding-top:2px}
.cart .title{font-family:'Roboto Condensed',sans-serif;font-size:12px;font-weight:700;line-height:13px}
.cart .count{font-size:9px;line-height:11px}
.cart .checkout{display:inline-block;margin-top:2px;background:var(--orange);font-family:'Roboto Condensed',sans-serif;font-size:9px;padding:2px 5px}

/* navigation */
.nav{height:38px;background:var(--green)}
.nav ul{list-style:none;display:flex;height:38px}
.nav li{border-right:1px solid rgba(255,255,255,.35);color:var(--white);font-size:10.5px;line-height:11px;padding:9px 8px 0;display:flex;gap:4px;text-transform:uppercase}
.nav li.home{background:var(--orange);justify-content:center;align-items:center;padding:0;border-left:1px solid rgba(255,255,255,.35)}
.nav li svg{flex:none;margin-top:1px}

/* hero */
.hero{height:367px;position:relative;overflow:hidden}
.hero .photo{position:absolute;inset:0;background:linear-gradient(120deg,#8a9a5a 0%,#c9b98a 30%,#e9d9c2 45%,#a7b5c2 60%,#8a8f84 100%)}
.hero .curve{position:absolute;inset:0}
.hero .copy{position:absolute;left:460px;width:310px;top:20px;text-align:center;color:var(--white);z-index:2}
.hero h1{font-family:'Cinzel',serif;font-weight:400;font-size:35px;line-height:38px;letter-spacing:1px}
.hero h1 b{font-family:'Roboto',sans-serif;font-weight:700}
.hero h2{font-family:'Roboto Condensed',sans-serif;font-weight:400;font-size:20px;line-height:22px;margin-top:2px}
.hero p{font-size:13px;line-height:18px;margin-top:2px}
.hero .cta{display:inline-block;margin-top:8px;background:var(--sky);font-family:'Roboto Condensed',sans-serif;font-weight:700;font-size:14px;line-height:18px;padding:5px 17px}
.hero .bottles{position:absolute;left:476px;top:152px;width:340px;height:210px;border-radius:60px 60px 8px 8px;background:linear-gradient(180deg,#f3f6e8 0%,#dfe9c6 35%,#7cae3c 65%,#3f7d2a 100%);z-index:1}

/* tabs */
.tabs{height:33px;border-bottom:1px solid var(--line)}
.tabs .wrap{height:33px;display:flex;align-items:stretch}
.tabs .arrow{width:32px;border-left:1px solid var(--line);border-right:1px solid var(--line);display:flex;align-items:center;justify-content:center}
.tabs .list{display:flex;gap:2px;margin-left:104px}
.tabs .tab{width:164px;font-family:'Raleway',sans-serif;font-size:18px;display:flex;align-items:center;justify-content:center;background:#e9e9e9;color:#555}
.tabs .tab.active{background:var(--green);color:var(--white)}
.tabs .arrow.next{margin-left:auto}

/* products */
.products{height:284px;background:var(--panel);padding-top:20px}
.products .wrap{display:flex;gap:19.3px}
.card{width:178px;height:242px;background:var(--white)}
.card .image{height:152px;border-bottom:1px solid #eee;display:flex;align-items:center;justify-content:center}
.card .image i{display:block;width:62px;height:120px;border-radius:14px}
.card .name{font-size:12.5px;font-weight:300;color:#333;line-height:15px;padding:13px 7px 0;height:54px}
.card .row{display:flex;justify-content:space-between;align-items:flex-end;padding:0 7px}
.card .was{font-size:10px;color:#888;text-decoration:line-through}
.card .now{font-size:13px;color:#111;font-weight:500}
.card .add{background:var(--orange);color:var(--white);font-family:'Roboto Condensed',sans-serif;font-size:12px;padding:4px 10px}

/* rewards */
.rewards{height:74px}
.rewards .wrap{display:flex;align-items:center;height:74px}
.rewards h3{font-family:'Roboto',sans-serif;font-weight:500;font-size:13px;line-height:13px;color:var(--ink);width:170px}
.rewards p{font-size:10px;line-height:15px;color:#444;width:300px}
.rewards form{margin-left:auto;display:flex;width:296px;height:27px}
.rewards .email{flex:1;border:1px solid #ccc;font-size:10px;color:#444;padding:0 7px;display:flex;align-items:center}
.rewards .join{width:59px;background:#000;color:var(--white);font-weight:700;font-size:12px;display:flex;align-items:center;justify-content:center}

/* benefits */
.benefits{height:70px;background:var(--sky-band);padding-top:13px}
.benefits .wrap{display:flex;gap:10px}
.benefit{width:185px;height:44px;background:var(--white);display:flex;align-items:center;gap:8px;padding-left:10px}
.benefit strong{display:block;font-family:'Roboto Condensed',sans-serif;font-weight:400;font-size:12px;color:var(--ink)}
.benefit span{font-size:10px;color:#444}

/* footer */
.footer{height:204px;background:var(--footer);padding-top:27px}
.footer .wrap{display:flex}
.col{width:198px}
.col h4{font-size:10.5px;font-weight:700;color:var(--ink);margin-bottom:7px}
.col li{list-style:none;font-size:10px;color:#555;line-height:19px}
.social{display:flex;gap:7px;margin-top:2px}
.social i{width:27px;height:27px;border-radius:50%;background:#777}
.pay{display:grid;grid-template-columns:35px 35px 35px;gap:5px;margin-top:-1px}
.pay i{height:21px;border-radius:2px;background:#1c4f9c}
.pay i:nth-child(2){background:#e9eef6}
.pay i:nth-child(3){background:#d1232a}
.pay i:nth-child(4){background:#2a79c4}
.pay i:nth-child(5){background:#f2e7dc}
.copyright{height:32px;text-align:center;font-size:10px;color:#555;line-height:32px;letter-spacing:.2px}
</style>
</head>
<body>

<div class="topbar">
  <div class="wrap">
    <div class="promo">Get Your <b>FREE</b> Promo Code Here</div>
    <div class="links">
      <span><svg viewBox="0 0 10 10"><circle cx="5" cy="3" r="2.2" fill="none" stroke="#777"/><path d="M1 10c0-3 2-4 4-4s4 1 4 4" fill="none" stroke="#777"/></svg>My Account</span>
      <span><svg viewBox="0 0 10 10"><circle cx="5" cy="3" r="2.2" fill="none" stroke="#777"/><path d="M1 10c0-3 2-4 4-4s4 1 4 4" fill="none" stroke="#777"/></svg>Log In &nbsp;/&nbsp; Register</span>
      <span><svg viewBox="0 0 10 10"><path d="M5 9L1.2 5A2.2 2.2 0 0 1 5 2.3 2.2 2.2 0 0 1 8.8 5z" fill="none" stroke="#777"/></svg>Wish List</span>
    </div>
  </div>
</div>

<header class="header">
  <div class="wrap">
    <div class="brand"><span class="dot"></span><span class="name">Nutri Harbour</span></div>
    <div class="search">
      <div class="field">Search entire store here...</div>
      <div class="btn"><svg width="14" height="14" viewBox="0 0 14 14"><circle cx="6" cy="6" r="4.3" fill="none" stroke="#fff" stroke-width="1.6"/><path d="M9.2 9.2L13 13" stroke="#fff" stroke-width="1.8"/></svg></div>
    </div>
    <div class="cart">
      <div class="icon"><svg width="36" height="30" viewBox="0 0 36 30"><path d="M1 3h6l4 16h18l4-12H9" fill="none" stroke="#fff" stroke-width="2"/><circle cx="14" cy="25" r="2.5" fill="none" stroke="#fff" stroke-width="2"/><circle cx="26" cy="25" r="2.5" fill="none" stroke="#fff" stroke-width="2"/></svg></div>
      <div class="info">
        <div class="title">MY CART</div>
        <div class="count">0 items</div>
        <span class="checkout">CHECKOUT</span>
      </div>
    </div>
  </div>
</header>

<nav class="nav">
  <ul class="wrap">
    <li class="home" style="width:38px"><svg width="14" height="14" viewBox="0 0 14 14"><path d="M1 7L7 1.5 13 7M3 6v7h8V6" fill="none" stroke="#fff" stroke-width="1.2"/><rect x="5.5" y="8.5" width="3" height="4.5" fill="none" stroke="#fff"/></svg></li>
    <li style="width:56px">Brand</li>
    <li style="width:104px">Supplements <svg width="10" height="8" viewBox="0 0 10 8"><path d="M1 2l4 4 4-4" fill="none" stroke="#fff" stroke-width="1.4"/></svg></li>
    <li style="width:88px;justify-content:space-between">Sports<br>Nutrition <svg width="10" height="8" viewBox="0 0 10 8"><path d="M1 2l4 4 4-4" fill="none" stroke="#fff" stroke-width="1.4"/></svg></li>
    <li style="width:86px">Haircare <svg width="10" height="8" viewBox="0 0 10 8"><path d="M1 2l4 4 4-4" fill="none" stroke="#fff" stroke-width="1.4"/></svg></li>
    <li style="width:98px">Chiropractic<br>Pillows</li>
    <li style="width:94px;justify-content:space-between">Health<br>Condition <svg width="10" height="8" viewBox="0 0 10 8"><path d="M1 2l4 4 4-4" fill="none" stroke="#fff" stroke-width="1.4"/></svg></li>
    <li style="width:84px">Beauty &amp;<br>Skincare <svg width="10" height="8" viewBox="0 0 10 8"><path d="M1 2l4 4 4-4" fill="none" stroke="#fff" stroke-width="1.4"/></svg></li>
    <li style="width:59px">Gluten<br>Free</li>
    <li style="width:63px;border-right:none">On Sale</li>
  </ul>
</nav>

<section class="hero">
  <div class="photo" role="img" aria-label="Photo of a smiling woman holding a glass of orange juice outdoors"></div>
  <svg class="curve" width="878" height="367" viewBox="0 0 878 367" preserveAspectRatio="none"><path d="M448 0C380 110 380 260 418 367H878V0z" fill="var(--orange-hero)"/></svg>
  <div class="copy">
    <h1>EXTRA <b>20%</b> OFF</h1>
    <h2>VITAMINS, SUPPLEMENTS</h2>
    <p>Use promo code: <b>NUTRI</b></p>
    <span class="cta">SHOP NOW ▸</span>
  </div>
  <div class="bottles" role="img" aria-label="Group of vitamin supplement bottles with yellow and white caps"></div>
</section>

<div class="tabs">
  <div class="wrap">
    <div class="arrow"><svg width="10" height="18" viewBox="0 0 10 18"><path d="M9 1L1 9l8 8" fill="none" stroke="#aaa"/></svg></div>
    <div class="list">
      <div class="tab active">Featured Product</div>
      <div class="tab">New Arrivals</div>
      <div class="tab">Our Best Sellers</div>
    </div>
    <div class="arrow next"><svg width="10" height="18" viewBox="0 0 10 18"><path d="M1 1l8 8-8 8" fill="none" stroke="#aaa"/></svg></div>
  </div>
</div>

<section class="products">
  <div class="wrap">
    <article class="card">
      <div class="image"><i role="img" aria-label="White supplement bottle" style="background:linear-gradient(180deg,#f2f2f2,#dfe6ee)"></i></div>
      <div class="name">Restwell Pillow Small Size Soft Density</div>
      <div class="row"><div><div class="was">$100</div><div class="now">$95.00</div></div><span class="add">ADD TO CART</span></div>
    </article>
    <article class="card">
      <div class="image"><i role="img" aria-label="White fiber and herb tablet bottle" style="background:linear-gradient(180deg,#f0f0f0,#d9e4cf)"></i></div>
      <div class="name">Restwell Pillow Standard Size Super Soft Density</div>
      <div class="row"><div><div class="was">$100</div><div class="now">$95.00</div></div><span class="add">ADD TO CART</span></div>
    </article>
    <article class="card">
      <div class="image"><i role="img" aria-label="Black jar of salty liquorice" style="width:96px;height:110px;border-radius:8px;background:linear-gradient(180deg,#2a2a2a,#111)"></i></div>
      <div class="name">Dreamsoft Deluxe Conventional Foam</div>
      <div class="row"><div><div class="was">$42.95</div><div class="now">$38.99</div></div><span class="add">ADD TO CART</span></div>
    </article>
    <article class="card">
      <div class="image"><i role="img" aria-label="Amber glass bottle of cedarwood essential oil" style="width:54px;background:linear-gradient(180deg,#3a2a1e,#8a5a2e 40%,#e8e2cf 60%,#5a3a22)"></i></div>
      <div class="name" style="padding-left:0">Cedarwood Oil</div>
      <div class="row"><div><div class="was">$14.99</div><div class="now">$11.99</div></div><span class="add">ADD TO CART</span></div>
    </article>
  </div>
</section>

<section class="rewards">
  <div class="wrap">
    <h3>JOIN<br>NUTRI HARBOUR REWARDS</h3>
    <p>Be rewarded with exclusive member offers, including discounts, sales, freebies, gifts-with purchase and competitions.</p>
    <form>
      <div class="email">Enter your email address</div>
      <div class="join">JOIN</div>
    </form>
  </div>
</section>

<section class="benefits">
  <div class="wrap">
    <div class="benefit">
      <svg width="26" height="18" viewBox="0 0 26 18" fill="none" stroke="var(--green)" stroke-width="1.3"><rect x="6" y="2" width="12" height="11"/><path d="M18 6h4l3 4v3h-7M1 5h4M2 8h4"/><circle cx="10" cy="15" r="2"/><circle cx="21" cy="15" r="2"/></svg>
      <div><strong>FREE SHIPPING</strong><span>for all orders over $99!</span></div>
    </div>
    <div class="benefit">
      <svg width="24" height="22" viewBox="0 0 24 22" fill="none" stroke="var(--green)" stroke-width="1.3"><path d="M2 8h20L20 2H4zM3 8v13h18V8M9 21v-7h6v7"/></svg>
      <div><strong>OFFICIAL STOCKIST</strong><span>of more than 100 brands</span></div>
    </div>
    <div class="benefit">
      <svg width="24" height="22" viewBox="0 0 24 22" fill="none" stroke="var(--green)" stroke-width="1.3"><rect x="2" y="6" width="8" height="15" rx="1"/><rect x="13" y="6" width="9" height="15" rx="1"/><path d="M3 3h6M14 3h7"/></svg>
      <div><strong>2 FREE SAMPLES</strong><span>on all orders over $99</span></div>
    </div>
    <div class="benefit">
      <svg width="24" height="24" viewBox="0 0 24 24" fill="none" stroke="var(--green)" stroke-width="1.3"><circle cx="12" cy="12" r="10.5"/><path d="M7 12l4 4 7-8" stroke-width="1.8"/></svg>
      <div><strong>VERIFIED TRUSTED STORE</strong><span>rating of 4.9/5</span></div>
    </div>
  </div>
</section>

<footer class="footer">
  <div class="wrap">
    <div class="col">
      <h4>CUSTOMER SERVICE</h4>
      <ul><li>Contact Us</li><li>Help &amp; FAQ</li><li>Order Tracking</li><li>Return Policy</li><li>Shipping Information</li><li>Shopping Cart</li><li>International Orders</li></ul>
    </div>
    <div class="col">
      <h4>ABOUT US</h4>
      <ul><li>Company Information</li><li>Employment</li><li>Affiliate Program</li><li>110% Lowest Price Guarantee</li><li>100% Happiness Guarantee</li><li>Our Family Of Brands</li><li>Company News</li></ul>
    </div>
    <div class="col">
      <h4>SAFE &amp; SECURE SHOPPING</h4>
      <ul><li>Security/Privacy</li><li>Terms &amp; Conditions</li><li>Your California Privacy Rights</li><li>Site Map</li><li>Safety News</li></ul>
    </div>
    <div class="col">
      <h4>FOLLOW US</h4>
      <div class="social"><i></i><i></i><i></i><i></i><i></i></div>
      <h4 style="margin-top:12px">WE ACCEPT</h4>
      <div class="pay"><i></i><i></i><i></i><i></i><i></i></div>
    </div>
  </div>
</footer>
<div class="copyright">© 2017 NUTRI HARBOUR. ALL RIGHTS RESERVED.</div>

</body>
</html>
```